TR Advisory Business Cards - High End AV / Low Voltage Company

We are low voltage AV company that specializes in high end clients on the residential side and larger businesses on the commercial side. We want something modern, tech looking but also something that is extremely professional looking. We have uploaded our logos and postcards we already have in the field. Along with a picture of one of our wrapped vans. Our website is at www.trvadvisory.example and our primary colors are the orange, green, grey and blue all military color finishes.

We are interesting in the slogans "Pairing You with the Right Technology" or "Leading the Lowcountry in Tech"

Target Market(s)

We focus on 70% Commercial and 30% Residential Customers

Industry/Entity Type

Low Voltage, AV Company

Contact Information for Business Card

Name - Dorian Fairweather, Title - Owner, Office Phone - 555-714-3096, Mobile Phone - 555-802-4173, E-Mail - d@trvadvisory.example, Website: www.trvadvisory.example

Font styles to use
Sans Serif

Requirements
Must have
• Must have Name, Title, Work Phone & Mobile, Website and Logo.
Nice to have
• We want something that will impress our higher end clients with a great logo
Should not have
• Too traditional or plain.

```html
<!DOCTYPE html>
<html lang="en">
<head>
<meta charset="utf-8">
<title>TR Advisory Business Cards</title>
<link rel="stylesheet" href="https://fonts.googleapis.com/css2?family=Ubuntu:wght@300;400;500;700&family=Heebo:wght@400&family=Montserrat:wght@700;800&display=swap">
<style>
  :root {
    --page-bg: #111112;
    --card-bg: #222226;
    --orange: #ec6a33;
    --white: #f4f4f4;
    --emboss: #18181b;
    --emboss-edge: #2e2e33;
    --van-green: #56643a;
    --van-dark: #2f3822;
  }
  * { margin: 0; padding: 0; box-sizing: border-box; }
  html, body {
    width: 1200px; height: 960px; overflow: hidden;
    background: var(--page-bg);
    font-family: "Ubuntu", sans-serif;
  }
  .card {
    position: absolute; left: 216px; width: 700px; height: 400px;
    background: var(--card-bg);
    border: 2.5px solid var(--orange);
    border-radius: 34px;
    overflow: hidden;
    box-shadow: 0 14px 30px rgba(0,0,0,.55);
  }
  .card-front { top: 60px; }
  .card-back { top: 501px; }

  /* front */
  .front-ring {
    position: absolute; left: 226px; top: 56px; width: 244px; height: 244px;
    border-radius: 50%;
    border: 14px solid var(--emboss);
    box-shadow: 0 0 0 1px var(--emboss-edge), inset 0 0 0 1px var(--emboss-edge);
    display: flex; align-items: center; justify-content: center;
    text-align: center;
  }
  .front-name {
    font-family: "Montserrat", sans-serif; font-weight: 800;
    font-size: 40px; line-height: 1.1; color: var(--emboss);
    text-shadow: 0 1px 0 var(--emboss-edge);
  }
  .front-phone {
    position: absolute; left: 0; right: 0; top: 312px;
    text-align: center;
    font-family: "Montserrat", sans-serif; font-weight: 800;
    font-size: 28px; line-height: 1; color: var(--emboss);
    text-shadow: 0 1px 0 var(--emboss-edge);
  }
  .tagline {
    position: absolute; left: 0; right: 0; top: 358px;
    text-align: center;
    font-family: "Heebo", sans-serif; font-size: 17px; line-height: 1;
    color: var(--orange);
  }

  /* back */
  .brand {
    position: absolute; left: 25px; top: 26px; width: 176px;
    text-align: center;
  }
  .brand-circle {
    width: 152px; height: 152px; margin: 0 auto;
    border-radius: 50%; border: 8px solid var(--orange);
    display: flex; align-items: center; justify-content: center;
  }
  .brand-name {
    font-family: "Montserrat", sans-serif; font-weight: 700;
    font-size: 22px; line-height: 1.1; color: var(--orange);
  }
  .brand-phone {
    margin-top: 12px;
    font-family: "Montserrat", sans-serif; font-weight: 700;
    font-size: 17px; line-height: 1; color: var(--orange);
  }
  .person {
    position: absolute; right: 24px; top: 22px; text-align: right;
  }
  .person-name {
    font-size: 35px; line-height: 1.1; color: var(--orange);
    letter-spacing: .3px; white-space: nowrap;
  }
  .person-name .first { font-weight: 700; }
  .person-name .last { font-weight: 300; }
  .person-title { font-size: 17px; color: var(--white); margin-top: 4px; letter-spacing: .5px; }
  .accent-bar {
    position: absolute; right: 0; top: 27px; width: 16px; height: 54px;
    background: var(--orange);
  }
  .contacts {
    position: absolute; left: 22px; top: 283px; list-style: none;
  }
  .contacts li {
    display: flex; align-items: center; height: 23.7px;
    font-size: 18px; color: var(--white); letter-spacing: .4px; white-space: nowrap;
  }
  .contacts svg { width: 16px; height: 16px; margin-right: 10px; fill: var(--orange); flex: none; }
  .van-photo {
    position: absolute; left: 360px; top: 236px; width: 342px; height: 164px;
    background: radial-gradient(ellipse at 60% 55%, var(--van-green) 0%, var(--van-dark) 70%, rgba(34,34,38,0) 100%);
  }
</style>
</head>
<body>

<section class="card card-front">
  <div class="front-ring"><span class="front-name">TR<br>Advisory</span></div>
  <div class="front-phone">555-714-3096</div>
  <p class="tagline">Pairing You with the Right Technology</p>
</section>

<section class="card card-back">
  <div class="brand">
    <div class="brand-circle"><span class="brand-name">TR<br>Advisory</span></div>
    <div class="brand-phone">555-714-3096</div>
  </div>

  <div class="person">
    <div class="person-name"><span class="first">Dorian</span> <span class="last">Fairweather</span></div>
    <div class="person-title">Owner</div>
  </div>
  <div class="accent-bar"></div>

  <ul class="contacts">
    <li><svg viewBox="0 0 16 16"><path d="M3.6 1.5l2.3 2.6-1.3 1.6c.9 2 2.5 3.7 4.6 4.7l1.6-1.3 2.6 2.3-1.5 2.1C6.8 13.3 2.5 9 1.5 3z"/></svg>555-714-3096</li>
    <li><svg viewBox="0 0 16 16"><path d="M4 1h8v14H4zM5.5 3v9h5V3zM7 13h2v1H7z" fill-rule="evenodd"/></svg>555-802-4173</li>
    <li><svg viewBox="0 0 16 16"><path d="M1 4h14v9H1zM2 5l6 4.5L14 5v-.2H2z" fill-rule="evenodd"/></svg>d@trvadvisory.example</li>
    <li><svg viewBox="0 0 16 16"><path d="M8 1a7 7 0 100 14A7 7 0 008 1zm-4 4l3 1 1 3-2 1v3a5.5 5.5 0 01-2-8zm5 8l1-3 2-1 1 2a5.5 5.5 0 01-4 2z"/></svg>www.trvadvisory.example</li>
  </ul>

  <div class="van-photo" role="img" aria-label="Photo of the company's green wrapped service van with a ladder on the roof rack"></div>
</section>

</body>
</html>
```